K.T.L Electrical Services Pty Ltd

Electrical contracting business. I have a base for the design which i like. The contact number needs to be changed to 0431862957 and the O made more solid and level with the rest of the letters. If you have any other ideas of what would make it better I'm happy to see them.

The back side to be written as dot points with the following:
- Residential & Commercial
- Maintenance
- PV & Battery servicing
- EV Chargers

```html
<!DOCTYPE html>
<html lang="en">
<head>
<meta charset="utf-8">
<title>K.T.L Electrical Services – Business Card</title>
<link rel="stylesheet" href="https://fonts.googleapis.com/css2?family=Outfit:wght@400;500&family=IBM+Plex+Sans:wght@400&display=swap">
<style>
  :root {
    --page: #ffffff;
    --card-base: #050909;
    --card-edge: #131c1d;
    --decor-light: #111a1b;
    --decor-dark: #050909;
    --ink: #8fa5a3;
    --shadow: rgba(0,0,0,0.18);
  }
  html, body {
    margin: 0;
    width: 1200px;
    height: 1200px;
    overflow: hidden;
    background: var(--page);
  }
  .sheet {
    position: relative;
    width: 1200px;
    height: 1200px;
  }
  .card {
    position: absolute;
    left: 346px;
    width: 516px;
    overflow: hidden;
    box-shadow: 0 1px 3px var(--shadow);
  }
  /* Front */
  .card--front {
    top: 259px;
    height: 334px;
    background: linear-gradient(90deg, var(--card-edge) 0%, #0e1617 100%);
  }
  .card__decor {
    position: absolute;
    left: 99px;
    top: 0;
    right: 0;
    bottom: 0;
    background: radial-gradient(ellipse 70% 80% at 60% 75%, var(--decor-dark) 0%, var(--decor-dark) 55%, var(--decor-light) 100%);
  }
  .card__phone {
    position: absolute;
    left: 42px;
    top: 135px;
    transform: translate(-50%, -50%) rotate(-90deg);
    font-family: "Outfit", sans-serif;
    font-weight: 500;
    font-size: 33px;
    letter-spacing: 2px;
    color: var(--ink);
    white-space: nowrap;
  }
  .brand {
    position: absolute;
    right: 42px;
    top: 126px;
    text-align: right;
    color: var(--ink);
    font-family: "Outfit", sans-serif;
  }
  .brand__name {
    display: block;
    font-weight: 500;
    font-size: 96px;
    line-height: 1;
    letter-spacing: 2px;
    margin-right: -4px;
  }
  .brand__descriptor {
    display: block;
    font-weight: 500;
    font-size: 19px;
    letter-spacing: 3.4px;
    margin-top: 4px;
    margin-right: -3px;
  }
  .brand__licence {
    display: block;
    font-family: "IBM Plex Sans", sans-serif;
    font-weight: 400;
    font-size: 21px;
    letter-spacing: 0.3px;
    margin-top: 4px;
  }
  /* Back */
  .card--back {
    top: 646px;
    height: 324px;
    background: var(--card-base);
  }
  .services {
    list-style: none;
    margin: 0;
    padding: 0;
    position: absolute;
    left: 42px;
    top: 37px;
    font-family: "IBM Plex Sans", sans-serif;
    font-size: 36px;
    line-height: 57px;
    color: var(--ink);
  }
  .services__item {
    position: relative;
    padding-left: 29px;
    white-space: nowrap;
  }
  .services__item::before {
    content: "";
    position: absolute;
    left: 2px;
    top: 25px;
    width: 9px;
    height: 9px;
    border-radius: 50%;
    background: var(--ink);
  }
</style>
</head>
<body>
<main class="sheet">
  <section class="card card--front" aria-label="Business card front">
    <div class="card__decor" role="img" aria-label="Decorative concentric arch pattern in dark charcoal tones"></div>
    <div class="card__phone">0431 862 957</div>
    <div class="brand">
      <span class="brand__name">K.T.L</span>
      <span class="brand__descriptor">ELECTRICAL SERVICES P/L</span>
      <span class="brand__licence">EC 27415</span>
    </div>
  </section>

  <section class="card card--back" aria-label="Business card back">
    <ul class="services">
      <li class="services__item">Residential &amp; Commercial</li>
      <li class="services__item">Maintenance</li>
      <li class="services__item">PV &amp; Battery servicing</li>
      <li class="services__item">EV Chargers</li>
    </ul>
  </section>
</main>
</body>
</html>
```